Trade Show Booth Sign Design for Retracting Banner

I need a trade show booth sign designed. It will be for a retractable banner that is double sided with 34 by 81 inch.

I want to incorporate my logo (see attached, have it in other file formats as well) and graphics from my website (https://www.dolbrookteachingadvisory.com/) with parts or all of the following text.

· Educational Content Creation
o Supplemental Textbook Content Development
o E-learning Content Development
· Curriculum Development
o KVTR/Bright Ladder
o Three Dimensional Learning
· Assessment
o Formative Assessments
o Elementary School, Middle School, High School, College, and Business
· Professional Development
o Training
o Facilitation

Target Market(s)

Education

Industry/Entity Type

Education

Font styles to use
Sans Serif

Colors

Designer to choose colors to be used in the design.

Requirements
Must have
• Eye catching and easy to read design
Nice to have
• Would like to see incorporation of my logo and some of the elements of my website images
Should not have
• N/A

```html
<!DOCTYPE html>
<html lang="en">
<head>
<meta charset="utf-8">
<title>Dolbrook Teaching Advisory – Retractable Banner</title>
<link href="https://fonts.googleapis.com/css2?family=Exo+2:wght@400;500;800;900&family=Montserrat:wght@700&display=swap" rel="stylesheet">
<style>
  :root{
    --stage:#a7a8ab;
    --chalk:#2b2b2b;
    --orange:#ee7710;
    --yellow:#f7e000;
    --blue:#3f86c6;
    --navy:#0a1f5c;
    --ring:#c9cbd0;
    --white:#ffffff;
  }
  *{box-sizing:border-box;margin:0;padding:0}
  html,body{width:1200px;height:1200px;overflow:hidden;background:var(--stage)}
  .stage{position:relative;width:1200px;height:1200px}
  .banner{position:absolute;top:127px;width:397px;height:945px;overflow:hidden;background:var(--white);font-family:"Exo 2",sans-serif}
  .banner--front{left:191px}
  .banner--back{left:612px}
  .banner__shapes{position:absolute;inset:0}
  .banner__photo{position:absolute;left:0;top:0;width:397px;height:117px;background:linear-gradient(180deg,#242424,#353535)}
  .brand{position:absolute;left:0;width:100%;text-align:center;color:var(--navy);font-weight:800}
  .brand__mark{position:absolute;left:148px;top:186px;width:100px;height:100px;border-radius:50%;background:#fbe27a}
  .brand__name{top:306px;font-size:46px;line-height:1;letter-spacing:.5px}
  .brand__tag{top:360px;font-size:18px;line-height:1}
  .section__title{position:absolute;color:var(--yellow);font-weight:800;font-size:19px;line-height:18px;text-transform:uppercase;letter-spacing:.3px}
  .list{position:absolute;list-style:none;color:var(--white);font-size:14px;line-height:16px;letter-spacing:.3px}
  .list li{position:relative;padding-left:11px;margin-bottom:5px}
  .list li::before{content:"";position:absolute;left:1px;top:6px;width:4px;height:4px;border-radius:50%;background:var(--yellow)}
  .list--center{left:0;width:100%;text-align:center}
  .list--center li{display:block;width:max-content;margin-left:auto;margin-right:auto}
  .badge{position:absolute;width:122px;height:122px;border-radius:50%;border:5px solid var(--ring);background:radial-gradient(circle at 50% 45%,#1d3a86,#0c1d55)}
  .site{position:absolute;left:0;bottom:0;width:100%;height:43px;background:var(--navy);color:var(--white);font-family:"Montserrat",sans-serif;font-weight:700;font-size:17px;line-height:43px;text-align:center;letter-spacing:.2px}
</style>
</head>
<body>
<div class="stage">

  <section class="banner banner--front">
    <svg class="banner__shapes" viewBox="0 0 397 945" aria-hidden="true">
      <polygon points="0,117 397,117 397,125 198,155 0,125" fill="var(--orange)"/>
      <polygon points="0,117 397,117 198,142" fill="var(--chalk)"/>
      <polygon points="0,285 43,320 0,355" fill="var(--yellow)"/>
      <polygon points="0,337 75,402 0,438" fill="var(--orange)"/>
      <polygon points="397,285 354,320 397,355" fill="var(--yellow)"/>
      <polygon points="397,337 322,402 397,438" fill="var(--orange)"/>
      <polygon points="0,438 198,397 397,438 397,945 0,945" fill="var(--blue)"/>
    </svg>
    <div class="banner__photo" role="img" aria-label="Chalkboard with crumpled colourful paper light bulbs hanging from drawn sockets"></div>

    <div class="brand__mark"></div>
    <div class="brand brand__name">DOLBROOK</div>
    <div class="brand brand__tag">Teaching Advisory</div>

    <h2 class="section__title" style="left:0;width:100%;text-align:center;top:443px">Educational Content Creation</h2>
    <ul class="list list--center" style="top:466px">
      <li>Supplemental Textbook Content Development</li>
      <li>E-learning Content Development</li>
    </ul>

    <div class="badge" style="left:29px;top:529px" role="img" aria-label="Illustration of a teacher presenting charts to a seated class"></div>
    <h2 class="section__title" style="left:167px;top:553px">Curriculum<br>Development</h2>
    <ul class="list" style="left:167px;top:593px">
      <li>KVTR/Bright Ladder</li>
      <li>Three Dimensional Learning</li>
    </ul>

    <div class="badge" style="left:29px;top:663px" role="img" aria-label="Illustration of science and learning icons around a flask"></div>
    <h2 class="section__title" style="left:167px;top:680px">Assessment</h2>
    <ul class="list" style="left:167px;top:703px;line-height:14.5px">
      <li>Formative Assessments</li>
      <li>Elementary School,<br>Middle School, High School,<br>College, and Business</li>
    </ul>

    <h2 class="section__title" style="left:0;width:100%;text-align:center;top:818px">Professional Development</h2>
    <ul class="list list--center" style="top:842px">
      <li>Training</li>
      <li>Facilitation</li>
    </ul>

    <div class="site">www.dolbrookteachingadvisory.com</div>
  </section>

  <section class="banner banner--back">
    <svg class="banner__shapes" viewBox="0 0 397 945" aria-hidden="true">
      <polygon points="0,117 397,117 397,125 198,155 0,125" fill="var(--orange)"/>
      <polygon points="0,117 397,117 198,142" fill="var(--chalk)"/>
      <polygon points="0,285 43,320 0,355" fill="var(--yellow)"/>
      <polygon points="0,337 75,402 0,438" fill="var(--orange)"/>
      <polygon points="397,285 354,320 397,355" fill="var(--yellow)"/>
      <polygon points="397,337 322,402 397,438" fill="var(--orange)"/>
      <polygon points="0,438 198,397 397,438 397,945 0,945" fill="var(--blue)"/>
    </svg>
    <div class="banner__photo" role="img" aria-label="Chalkboard with crumpled colourful paper light bulbs hanging from drawn sockets"></div>

    <div class="brand__mark"></div>
    <div class="brand brand__name">DOLBROOK</div>
    <div class="brand brand__tag">Teaching Advisory</div>

    <h2 class="section__title" style="left:0;width:100%;text-align:center;top:443px">Educational Content Creation</h2>
    <ul class="list list--center" style="top:466px">
      <li>Supplemental Textbook Content Development</li>
      <li>E-learning Content Development</li>
    </ul>

    <div class="badge" style="left:29px;top:529px" role="img" aria-label="Illustration of a teacher presenting charts to a seated class"></div>
    <h2 class="section__title" style="left:167px;top:553px">Curriculum<br>Development</h2>
    <ul class="list" style="left:167px;top:593px">
      <li>KVTR/Bright Ladder</li>
      <li>Three Dimensional Learning</li>
    </ul>

    <div class="badge" style="left:29px;top:663px" role="img" aria-label="Illustration of science and learning icons around a flask"></div>
    <h2 class="section__title" style="left:167px;top:680px">Assessment</h2>
    <ul class="list" style="left:167px;top:703px;line-height:14.5px">
      <li>Formative Assessments</li>
      <li>Elementary School,<br>Middle School, High School,<br>College, and Business</li>
    </ul>

    <h2 class="section__title" style="left:0;width:100%;text-align:center;top:818px">Professional Development</h2>
    <ul class="list list--center" style="top:842px">
      <li>Training</li>
      <li>Facilitation</li>
    </ul>

    <div class="site">www.dolbrookteachingadvisory.com</div>
  </section>

</div>
</body>
</html>
```